Tidal Crumb Ingredients

Ingredients list/einkorn info. We are looking to improve a 5.5 x 8.5" double sided handout (2 per 8.5 x 11" piece of paper) to hand out with bread and for marketing. Or skinnier 3 per piece of paper? Or suggest a better format. Also to be used in social media and web. And possibly a banner.

Target Market(s)

Healthy, intelligent, yoga, athletic, wealthy

Industry/Entity Type

Bakery

Font styles to use
Sans Serif
Other font styles liked:
• simple readable attractive

Requirements
Must have
• Display the value (and uniqueness) of ingredients
Nice to have
• Well presented info with instant visual appeal. Choose between the 2 logos which you like most. Let us know if you want more photos.
Should not have
• Ornate frills

```html
<!DOCTYPE html>
<html lang="en">
<head>
<meta charset="utf-8">
<title>Tidal Crumb – Ingredients &amp; Einkorn Handout</title>
<link rel="stylesheet" href="https://fonts.googleapis.com/css2?family=Montserrat:ital,wght@0,400;0,500;0,600;0,700;0,800;1,700;1,800&family=Poppins:wght@500;600;700;800&display=swap">
<style>
  :root{
    --backdrop:#cbc3c1;
    --frame:#6b2114;
    --espresso:#4a2a24;
    --maroon:#6a1f12;
    --orange:#f07a1a;
    --peach-light:#f3d7b8;
    --peach:#e4b48c;
    --panel:rgba(196,150,120,.35);
    --rule:#a07866;
    --bread:#9b7656;
    --bread-dark:#6f4f37;
    --paper:#ffffff;
    --white:#ffffff;
  }
  *{box-sizing:border-box;margin:0;padding:0}
  html,body{width:1200px;height:1200px;overflow:hidden}
  body{background:var(--backdrop);position:relative;font-family:"Montserrat",sans-serif}

  .card{position:absolute;width:397px;height:692px;border:7px solid var(--frame);overflow:hidden}
  .card--ingredients{left:196px;top:196px;
    background:radial-gradient(ellipse at 50% 45%, var(--peach-light) 0%, var(--peach) 75%)}
  .card--einkorn{left:631px;top:315px;background:var(--paper)}
  .card *{position:absolute}

  /* ---------- ingredients side ---------- */
  .brand-tab{left:140px;top:0;width:103px;height:108px;background:var(--white);
    border-radius:0 0 52px 52px;display:flex;align-items:center;justify-content:center;
    font:700 13px/1.1 "Montserrat",sans-serif;color:var(--maroon);text-align:center}
  .wheat-deco{background:rgba(120,70,45,.12);border-radius:8px}
  .bread-photo{background:linear-gradient(135deg,var(--bread) 0%,var(--bread-dark) 100%);border-radius:10px}
  .card--ingredients .bread-photo{left:240px;top:84px;width:134px;height:150px;transform:rotate(8deg)}

  .headline{left:56px;top:130px;color:var(--maroon);font-family:"Montserrat",sans-serif}
  .headline .lead{position:static;display:block;font-weight:700;font-size:17px;line-height:16px}
  .headline .big{position:static;display:block;font-weight:800;font-size:44px;line-height:44px;letter-spacing:-.5px}

  .tagline{left:45px;top:255px;width:297px;height:28px;background:var(--espresso);border-radius:5px;
    color:var(--orange);font:600 15px/28px "Montserrat",sans-serif;text-align:center}

  .ingredient-panel{left:45px;top:288px;width:297px;height:277px;background:var(--panel);border-radius:6px}
  .ingredient{left:0;width:297px}
  .ingredient .icon{left:12px;top:4px;width:34px;height:34px}
  .ingredient h3{left:58px;top:0;font:800 11px/14px "Montserrat",sans-serif;color:var(--espresso);white-space:nowrap}
  .ingredient p{left:58px;top:15px;width:232px;font:500 9px/11px "Montserrat",sans-serif;color:var(--orange)}
  .ingredient p small{position:static;font-size:8.4px;font-weight:400}
  .divider{left:7px;width:283px;height:1px;background:var(--rule)}
  .with-note{left:0;top:234px;width:297px;text-align:center;color:var(--white);
    font:500 9px/12px "Montserrat",sans-serif}

  .tolerance{left:45px;top:569px;width:297px;height:28px;background:var(--espresso);border-radius:5px;
    color:var(--orange);font:600 10.5px/11px "Montserrat",sans-serif;text-align:center;padding-top:3px}
  .celiac{left:0;top:602px;width:383px;text-align:center;color:var(--orange);font:500 9px "Montserrat",sans-serif}
  .card--ingredients .email{left:0;top:620px;width:383px;text-align:center;color:var(--espresso);font:500 12px "Montserrat",sans-serif}
  .contact-rule{left:70px;top:638px;width:243px;height:1px;background:var(--rule)}
  .card--ingredients .phone{left:0;top:641px;width:383px;text-align:center;color:var(--white);font:800 22px "Poppins",sans-serif;letter-spacing:.5px}

  /* ---------- einkorn side ---------- */
  .card--einkorn .bread-photo{left:100px;top:24px;width:190px;height:212px;transform:rotate(-4deg)}
  .einkorn-title{left:0;top:240px;width:383px;text-align:center;color:var(--maroon);
    font:700 42px/50px "Poppins",sans-serif;letter-spacing:-.3px}
  .title-rule{left:50px;top:298px;width:283px;height:1px;background:linear-gradient(90deg,transparent,var(--rule),transparent)}
  .subtitle{left:0;top:303px;width:383px;text-align:center;color:var(--maroon);font:600 13.5px "Poppins",sans-serif}
  .intro{left:30px;top:330px;width:323px;text-align:center;color:var(--maroon);font:600 10.5px/14px "Montserrat",sans-serif}
  .list-label{left:37px;top:381px;color:var(--maroon);font:600 10.5px "Montserrat",sans-serif}
  .benefits{left:37px;top:401px;width:320px;list-style:none;color:var(--maroon);font:500 11.3px/14px "Montserrat",sans-serif}
  .benefits li{position:relative;padding-left:16px;margin-bottom:0}
  .benefits li::before{content:"\25AA";position:absolute;left:0;top:0;font-size:9px}
  .gluten-note{left:30px;top:584px;width:323px;text-align:center;color:var(--maroon);font:700 11.5px/14px "Montserrat",sans-serif}
  .gluten-note em{position:static;font-style:italic;font-weight:800}
  .contact-box{left:50px;top:622px;width:297px;height:50px;background:var(--espresso);border-radius:5px}
  .contact-box .email{left:0;top:5px;width:297px;text-align:center;color:var(--white);font:500 9.5px "Montserrat",sans-serif}
  .contact-box .box-rule{left:15px;top:20px;width:267px;height:1px;background:rgba(255,255,255,.15)}
  .contact-box .phone{left:0;top:19px;width:297px;text-align:center;color:var(--orange);font:800 22px "Poppins",sans-serif;letter-spacing:.5px}
</style>
</head>
<body>

<section class="card card--ingredients">
  <div class="wheat-deco" role="img" aria-label="Line drawing of wheat stalks" style="left:8px;top:6px;width:100px;height:110px"></div>
  <div class="wheat-deco" role="img" aria-label="Line drawing of seeds and wheat" style="left:320px;top:6px;width:60px;height:60px"></div>
  <div class="wheat-deco" role="img" aria-label="Faint wheat ear outline" style="left:0;top:290px;width:40px;height:170px"></div>
  <div class="wheat-deco" role="img" aria-label="Line drawing of seeds and leaves" style="left:6px;top:615px;width:90px;height:60px"></div>
  <div class="wheat-deco" role="img" aria-label="Line drawing of wheat stalks" style="left:325px;top:560px;width:55px;height:115px"></div>

  <div class="brand-tab">Tidal<br>Crumb</div>
  <div class="bread-photo" role="img" aria-label="Three slices of marbled einkorn bread"></div>

  <h1 class="headline"><span class="lead">The</span><span class="lead">transformation of</span><span class="big">BREAD</span></h1>

  <div class="tagline">Nutritious I Digestible I Delicious</div>

  <div class="ingredient-panel">
    <div class="ingredient" style="top:6px">
      <svg class="icon" viewBox="0 0 34 34" fill="none" stroke="#6a1f12" stroke-width="1.2"><path d="M17 30V14M17 18c-5-1-7-6-6-10 4 1 6 5 6 10zM17 16c3-3 6-4 9-3-1 4-5 5-9 5"/><path d="M6 30h22M10 30c2-3 12-3 14 0"/></svg>
      <h3>Sprouted grains:</h3>
      <p>Einkorn, spelt, and a touch of heritage rye<br><small>(Organically grown on family farms<br>in Winthrop, Washington and Teton Valley, Idaho)</small></p>
    </div>
    <div class="divider" style="top:68px"></div>
    <div class="ingredient" style="top:73px">
      <svg class="icon" viewBox="0 0 34 34" fill="none" stroke="#6a1f12" stroke-width="1.2"><ellipse cx="13" cy="12" rx="6" ry="9"/><ellipse cx="21" cy="22" rx="6" ry="9"/><path d="M21 14c-2 5 2 11 0 16"/></svg>
      <h3>Seeds:</h3>
      <p style="font-size:9.4px;line-height:11.5px">Amaranth, sprouted pumpkin seeds, sprouted quinoa, chia seeds, flaxseed, hemp hearts, sprouted sunflowers seeds</p>
    </div>
    <div class="divider" style="top:136px"></div>
    <div class="ingredient" style="top:143px">
      <svg class="icon" viewBox="0 0 34 34" fill="none" stroke="#6a1f12" stroke-width="1.2"><path d="M17 28V12M17 14c-4-4-9-3-10 0 4 3 8 2 10 0zM17 12c3-4 8-5 11-3-2 4-7 5-11 3"/><path d="M5 24h8M9 28h10M5 20h6"/></svg>
      <h3 style="top:15px">Adaptogens:</h3>
      <p style="top:28px">Ashwaganda, Maca root</p>
    </div>
    <div class="divider" style="top:183px"></div>
    <div class="ingredient" style="top:192px">
      <svg class="icon" viewBox="0 0 34 34" fill="none" stroke="#6a1f12" stroke-width="1.2"><path d="M3 14c2-7 26-7 28 0-6 3-22 3-28 0z"/><path d="M12 16l-2 12h14l-2-12"/></svg>
      <h3 style="top:2px">Mushroom extracts:</h3>
      <p style="top:17px">Lions mane, cordycept</p>
    </div>
    <div class="divider" style="top:229px"></div>
    <p class="with-note">With:<br>Montana glacier well water, Cacao, MCT oil,<br>psyilium husk, Himalayan sea salt, trace minerals, Love</p>
  </div>

  <div class="tolerance">This bread is well<br>tolerated by people with gluten sensitivities.</div>
  <p class="celiac">(not for celiac disease)</p>
  <p class="email">hello@tidalcrumb.com</p>
  <div class="contact-rule"></div>
  <p class="phone">406-555-0142</p>
</section>

<section class="card card--einkorn">
  <div class="bread-photo" role="img" aria-label="Three slices of marbled einkorn bread"></div>
  <h2 class="einkorn-title">Einkorn grain</h2>
  <div class="title-rule"></div>
  <p class="subtitle">vs ‘modern wheat’</p>
  <p class="intro">Einkorn is the original, non-altered wheat grain.<br>It’s genetic purity is over 10,000 years old.</p>
  <p class="list-label">Einkorn is:</p>
  <ul class="benefits">
    <li>25% higher in protein and lower in carbohy-drates than modern wheat</li>
    <li>3-4 times more beta-carotene</li>
    <li>2 times more vitamin A</li>
    <li>4 times more antioxidants lutein and riboflavin.</li>
    <li>5-6 times more expensive $$$</li>
    <li>Richer in carotenoids, B vitamins, and essential and trace minerals</li>
    <li>Non-processed, non-hybridized, non-GMO, non-mutated and has a low glycemic load, meaning it won’t spike your blood sugar level.</li>
    <li>And it tastes better.</li>
  </ul>
  <p class="gluten-note">Einkorn <em>lacks the gluten proteins that trigger<br>symptoms of gluten sensitivity.</em></p>
  <div class="contact-box">
    <p class="email">hello@tidalcrumb.com</p>
    <div class="box-rule"></div>
    <p class="phone">406-555-0142</p>
  </div>
</section>

</body>
</html>
```